Introduction:
We are an Australia-based Cyber Security Penetration testing company seeking a website redesign to showcase our services, expertise, and experience. Our target audience includes businesses and organizations of all sizes who are seeking to secure their IT infrastructure against cyber threats. The purpose of the website redesign is to increase our online presence, generate leads, and establish our company as a trusted authority in the industry.
Objectives:
Create a professional and modern website that is easy to navigate and user-friendly.
Provide information about our company, services, and expertise.
Clearly display table of our 3 services: Bug Bounty as a Service, Penetration Testing and Code Review.
Generate leads through online contact forms and calls-to-action.
Optimize the website for search engines to increase visibility and traffic.
Website similar to: https://www.velmora.com.au/.
Target Audience:
Our target audience includes businesses and organizations of all sizes that require cybersecurity penetration testing services. These include:
Small and medium-sized enterprises (SMEs)
Australian Government agencies
Design Requirements:
Clean, modern, and professional design.
Use of colors that convey trust, reliability, and expertise (such as orange and grey).
Calls-to-action that encourage visitors to contact us or request a quote.
Integration with social media channels to increase engagement and brand awareness.
A blog section to showcase our thought leadership and expertise.
A news section to share updates about our company and the industry.
Content Requirements:
Home page that introduces our company and services and highlights our expertise.
About Us page that provides information about our company, team, and values.
Services page that lists our services and explains the benefits of each.
Case Studies page that showcases our previous work and success stories.
Contact Us page that includes a contact form, phone number, and email address.
Blog section with articles related to the cybersecurity industry and our services.
News section with updates about our company and the industry.

```html
<!DOCTYPE html>
<html lang="en">
<head>
<meta charset="utf-8">
<title>Cindervault – Cyber Security</title>
<link href="https://fonts.googleapis.com/css2?family=Exo+2:wght@500;600;700&family=Poppins:wght@400;500;600&display=swap" rel="stylesheet">
<style>
:root{
  --orange:#f07a1e;
  --orange-dark:#d9650d;
  --navy:#0c1a35;
  --ink:#1b1b1b;
  --text:#555b66;
  --light:#f6f7f9;
  --peach:#fdf3ea;
  --line:#e3e5ea;
  --white:#ffffff;
  --footer:#1c1c1e;
}
*{box-sizing:border-box;margin:0;padding:0}
html,body{width:1200px;height:4580px;overflow:hidden}
body{font-family:"Poppins",sans-serif;color:var(--text);background:var(--white);font-size:13px;line-height:1.6}
h1,h2,h3,h4,.brand{font-family:"Exo 2",sans-serif;color:var(--ink)}
.accent{color:var(--orange)}
section,header,footer{position:relative;width:1200px}
.abs{position:absolute}
.btn{display:inline-block;background:var(--orange);color:var(--white);font-size:11px;font-weight:600;letter-spacing:.5px;text-transform:uppercase;padding:10px 22px;border-radius:3px}
.underline-mark{display:flex;gap:4px;margin:10px 0 18px}
.underline-mark span{height:3px;background:var(--orange);border-radius:2px}
.underline-mark span:first-child{width:26px}.underline-mark span:last-child{width:8px}

/* hero */
.hero{height:520px;background:linear-gradient(100deg,#2b1a14 0%,#4a2a1c 40%,#6a4a3a 70%,#8a6d5a 100%)}
.hero-photo{inset:0;background:linear-gradient(180deg,rgba(240,122,30,.25),rgba(12,26,53,.55))}
.nav{left:160px;right:70px;top:28px;display:flex;justify-content:space-between;align-items:center}
.brand{display:flex;align-items:center;gap:10px;font-size:28px;font-weight:700;color:var(--white)}
.brand i{width:30px;height:30px;border-radius:50%;background:var(--orange);display:block}
.nav ul{display:flex;gap:30px;list-style:none;font-size:12px;font-weight:500;color:var(--white)}
.hero h1{left:160px;top:120px;width:560px;font-size:44px;line-height:1.2;color:var(--white);font-weight:700}
.hero p{left:160px;top:300px;width:430px;color:#e9e2dc;font-size:13px}
.hero-actions{left:160px;top:440px;display:flex;align-items:center;gap:20px;color:var(--white);font-size:12px}
.hero-actions .mail{display:flex;align-items:center;gap:8px}

/* about */
.about{height:540px}
.about-photo{left:140px;top:60px;width:460px;height:440px;border-radius:120px 120px 60px 160px;background:linear-gradient(135deg,#dce6f2,#3a5a8a 55%,#0d1d3c)}
.about-text{left:628px;top:150px;width:420px}
.about-text h2{font-size:32px}
.stats{display:flex;gap:40px;margin:22px 0 26px}
.stat b{display:block;font-family:"Exo 2",sans-serif;font-size:22px;color:var(--orange)}
.stat span{font-size:10px;color:var(--ink)}

/* services */
.services{height:452px}
.services-text{left:160px;top:90px;width:360px}
.services-text h2{font-size:32px}
.services-text .btn{margin-top:22px}
.svc{width:190px;background:var(--white);border-radius:6px;box-shadow:0 6px 24px rgba(0,0,0,.09);display:flex;flex-direction:column;align-items:center;justify-content:center;gap:14px;font-family:"Exo 2",sans-serif;font-weight:700;font-size:17px;color:var(--ink);text-align:center}
.svc svg{width:54px;height:54px}
.svc.featured{background:var(--orange);color:var(--white)}

/* ops */
.ops{height:388px;background:var(--navy)}
.ops-art{left:700px;top:0;width:420px;height:388px;background:radial-gradient(circle at 55% 50%,#2e6bd6 0%,#163a7a 40%,var(--navy) 75%)}
.ops h2{left:160px;top:108px;font-size:32px;color:var(--white)}
.ops p{left:160px;top:162px;width:500px;color:#c6cfdf;font-size:12px}
.ops ul{left:160px;top:222px;width:440px;list-style:none;display:grid;grid-template-columns:1fr 1fr;gap:8px 20px;color:var(--white);font-size:12px}
.ops li{display:flex;align-items:center;gap:8px}
.ops li::before{content:"";width:7px;height:7px;background:var(--orange);border-radius:50%}

/* pricing */
.pricing{height:720px}
.sec-title{left:0;right:0;text-align:center}
.sec-title h2{font-size:32px}
.sec-title .underline-mark{justify-content:center}
.sec-title p{width:600px;margin:0 auto;font-size:13px}
.plan{top:210px;width:260px;height:440px;background:var(--white);border-radius:8px;box-shadow:0 8px 28px rgba(0,0,0,.1);overflow:hidden;text-align:center}
.plan-head{height:130px;background:var(--ink);padding-top:18px}
.plan-head h3{color:var(--white);font-size:24px}
.plan.featured .plan-head{background:var(--orange)}
.price{width:150px;margin:10px auto 0;background:var(--orange);border-radius:4px;padding:6px 0;color:var(--white)}
.plan.featured .price{background:var(--white);color:var(--orange)}
.price b{font-family:"Exo 2",sans-serif;font-size:30px;line-height:1;display:block}
.price span{font-size:9px}
.plan ul{list-style:none;text-align:left;padding:26px 24px 0;font-size:11px;color:var(--ink)}
.plan li{display:flex;gap:10px;align-items:center;padding:7px 0;border-bottom:1px solid var(--line);white-space:nowrap}
.plan li svg{width:12px;height:12px;flex:none}
.plan .btn{position:absolute;left:50%;transform:translateX(-50%);bottom:26px}

/* blogs */
.blogs{height:660px}
.blog-grid{left:160px;top:210px;width:860px;display:grid;grid-template-columns:220px 200px 220px 200px;grid-template-rows:160px 160px;column-gap:10px;row-gap:0}
.blog-img{position:relative;background:linear-gradient(135deg,#2a3850,#0f1a2e 60%,#d06a22)}
.blog-img .date{position:absolute;right:0;bottom:14px;background:var(--orange);color:var(--white);font-size:9px;font-weight:600;padding:4px 8px;text-align:center;line-height:1.2}
.blog-txt{padding:12px 10px}
.blog-txt h4{font-size:13px;line-height:1.3;margin-bottom:6px}
.blog-txt p{font-size:10px;line-height:1.5}
.read{font-size:10px;color:var(--orange);font-weight:600;text-transform:uppercase;display:block;margin-top:6px}
.blogs .btn{left:50%;transform:translateX(-50%);top:570px}

/* news */
.news{height:440px;background:var(--peach)}
.news-card{top:70px;width:280px;height:300px;background:var(--white);box-shadow:0 6px 20px rgba(0,0,0,.06)}
.news-card .img{height:160px;background:linear-gradient(135deg,#1a2538,#3a4a6a 50%,#c86a2a)}
.news-card .meta{display:flex;justify-content:space-between;font-size:10px;padding:10px 16px}
.news-card h4{font-size:15px;text-align:center;padding:0 24px;line-height:1.3}
.news-card .read{text-align:center}
.arrow{top:200px;width:26px;height:26px;border-radius:50%;background:var(--white);box-shadow:0 2px 8px rgba(0,0,0,.1);display:flex;align-items:center;justify-content:center;z-index:2}
.news-head{left:800px;top:150px}
.news-head h2{font-size:40px}

/* contact */
.contact{height:420px}
.form{left:200px;top:140px;width:800px;display:grid;grid-template-columns:1fr 1fr;gap:16px 40px}
.field{height:44px;border:1px solid var(--line);background:var(--light);border-radius:3px;display:flex;align-items:center;gap:10px;padding:0 14px;font-size:11px;color:#8a8f98}
.field.tall{grid-row:span 2;height:104px;align-items:flex-start;padding-top:14px}
.field svg{width:12px;height:12px;flex:none}
.contact .btn{left:50%;transform:translateX(-50%);top:340px}

/* footer */
.footer{height:400px;background:var(--footer);color:#b9bcc2}
.footer .brand{left:160px;top:60px;position:absolute}
.footer .about-f{left:160px;top:110px;width:240px;font-size:11px}
.socials{left:160px;top:200px;display:flex;gap:10px}
.socials i{width:26px;height:26px;border-radius:50%;background:#34353a;display:block}
.fcol{top:60px}
.fcol h4{color:var(--white);font-size:15px;margin-bottom:14px}
.fcol ul{list-style:none;font-size:11px}
.fcol li{padding:3px 0}
.fcol li.on{color:var(--white)}
.contact-list li{display:flex;gap:10px;padding:6px 0}
.contact-list svg{width:22px;height:22px;flex:none}
.contact-list b{display:block;color:var(--white);font-weight:500}
.copyright{left:0;right:0;bottom:0;height:60px;background:var(--orange);color:var(--white);text-align:center;line-height:60px;font-size:12px}
</style>
</head>
<body>

<header class="hero">
  <div class="abs hero-photo" role="img" aria-label="Night city skyline with harbour bridge under warm orange glow"></div>
  <nav class="abs nav">
    <div class="brand"><i></i>Cindervault</div>
    <ul><li>About</li><li>Services</li><li>Case Studies</li><li>Blog</li><li>News</li><li>Contact Us</li></ul>
  </nav>
  <h1 class="abs">The Best <span class="accent">Cindervault</span> Service Provider In Country</h1>
  <p class="abs">Lorem ipsum dolor sit amet, consectetuer adipiscing elit, sed diam nonummy nibh euismod tincidunt ut laoreet dolore magna aliquam erat volutpat.</p>
  <div class="abs hero-actions">
    <span class="btn">Contact Us</span>
    <span class="mail"><svg width="26" height="26" viewBox="0 0 26 26"><rect width="26" height="26" rx="3" fill="#f07a1e"/><rect x="6" y="8" width="14" height="10" fill="none" stroke="#fff" stroke-width="1.5"/><path d="M6 8l7 6 7-6" fill="none" stroke="#fff" stroke-width="1.5"/></svg>info@cindervault.com</span>
  </div>
</header>

<section class="about">
  <div class="abs about-photo" role="img" aria-label="Security analysts at screens beside a glowing cloud shield"></div>
  <div class="abs about-text">
    <h2>About <span class="accent">Us</span></h2>
    <div class="underline-mark"><span></span><span></span></div>
    <p>Lorem ipsum dolor sit amet, consectetuer adipiscing elit, sed diam nonummy nibh euismod tincidunt ut laoreet dolore magna aliquam erat volutpat. Ut wisi enim ad minim veniam, quis nostrud exerci tation ullamcorper suscipit lobortis nisl ut aliquip ex ea commodo consequat.</p>
    <div class="stats">
      <div class="stat"><b>3k+</b><span>Cyber Security Projects</span></div>
      <div class="stat"><b>12,502</b><span>Global Customers</span></div>
      <div class="stat"><b>100+</b><span>Cyber Security Expert</span></div>
    </div>
    <span class="btn">Read More</span>
  </div>
</section>

<section class="services">
  <div class="abs services-text">
    <h2>Our <span class="accent">Services</span></h2>
    <div class="underline-mark"><span></span><span></span></div>
    <p>Lorem ipsum dolor sit amet, consectetuer adipiscing elit, sed diam nonummy nibh euismod tincidunt ut laoreet dolore magna aliquam erat volutpat. Ut wisi enim ad minim veniam.</p>
    <span class="btn">View All</span>
  </div>
  <div class="abs svc" style="left:600px;top:60px;height:170px">
    <svg viewBox="0 0 54 54"><path d="M27 6l17 7v12c0 12-8 20-17 23-9-3-17-11-17-23V13z" fill="none" stroke="#f07a1e" stroke-width="2.5"/><circle cx="27" cy="27" r="6" fill="#f07a1e"/></svg>Bug Bounty</div>
  <div class="abs svc featured" style="left:820px;top:0;height:200px">
    <svg viewBox="0 0 54 54"><rect x="12" y="24" width="30" height="22" rx="3" fill="none" stroke="#fff" stroke-width="2.5"/><path d="M18 24v-6a9 9 0 0118 0v6" fill="none" stroke="#fff" stroke-width="2.5"/></svg>Penetration<br>Testing</div>
  <div class="abs svc" style="left:600px;top:244px;height:176px">
    <svg viewBox="0 0 54 54"><path d="M20 16L9 27l11 11M34 16l11 11-11 11" fill="none" stroke="#f07a1e" stroke-width="2.5"/></svg>Code Review</div>
  <div class="abs svc" style="left:820px;top:214px;height:166px">
    <svg viewBox="0 0 54 54"><ellipse cx="27" cy="14" rx="14" ry="5" fill="none" stroke="#f07a1e" stroke-width="2.5"/><path d="M13 14v24c0 3 6 5 14 5s14-2 14-5V14M13 26c0 3 6 5 14 5s14-2 14-5" fill="none" stroke="#f07a1e" stroke-width="2.5"/></svg>Data Services</div>
</section>

<section class="ops">
  <div class="abs ops-art" role="img" aria-label="Glowing blue cloud with security lock on circuit board"></div>
  <h2 class="abs">24/7 Cyber Security <span class="accent">Operations Center</span></h2>
  <p class="abs">Lorem ipsum dolor sit amet, consectetuer adipiscing elit, sed diam conse.</p>
  <ul class="abs">
    <li>Testing Cyber Security</li><li>Website Hack Repair</li>
    <li>Managing Cloud Security</li><li>24/7 Security Support</li>
    <li>Server Security</li>
  </ul>
</section>

<section class="pricing">
  <div class="abs sec-title" style="top:70px">
    <h2>Our <span class="accent">Pricing</span></h2>
    <div class="underline-mark"><span></span><span></span></div>
    <p>Lorem ipsum dolor sit amet, consectetuer adipiscing elit, sed diam nonummy nibh euismod tincidunt ut laoreet dolore magna aliquam erat volutpat.</p>
  </div>
  <div class="abs plan" style="left:160px">
    <div class="plan-head"><h3>Pro</h3><div class="price"><b>$12</b><span>per user/per month</span></div></div>
    <ul>
      <li><svg viewBox="0 0 12 12"><path d="M2 6l3 3 5-6" fill="none" stroke="#f07a1e" stroke-width="2"/></svg>Real-time email tracking</li>
      <li><svg viewBox="0 0 12 12"><path d="M2 6l3 3 5-6" fill="none" stroke="#f07a1e" stroke-width="2"/></svg>Presentation tracking &amp; analytics</li>
      <li><svg viewBox="0 0 12 12"><path d="M2 6l3 3 5-6" fill="none" stroke="#f07a1e" stroke-width="2"/></svg>Personal templates &amp; reports</li>
      <li><svg viewBox="0 0 12 12"><path d="M2 6l3 3 5-6" fill="none" stroke="#f07a1e" stroke-width="2"/></svg>Send Later &amp; Reminders</li>
      <li><svg viewBox="0 0 12 12"><path d="M2 6l3 3 5-6" fill="none" stroke="#f07a1e" stroke-width="2"/></svg>Next Book A Time</li>
    </ul>
    <span class="btn">Buy Now</span>
  </div>
  <div class="abs plan featured" style="left:470px">
    <div class="plan-head"><h3>Premium</h3><div class="price"><b>$25</b><span>per user/per month</span></div></div>
    <ul>
      <li><svg viewBox="0 0 12 12"><path d="M2 6l3 3 5-6" fill="none" stroke="#f07a1e" stroke-width="2"/></svg>Includes Pro features and...</li>
      <li><svg viewBox="0 0 12 12"><path d="M2 6l3 3 5-6" fill="none" stroke="#f07a1e" stroke-width="2"/></svg>Team template sharing &amp; reporting</li>
      <li><svg viewBox="0 0 12 12"><path d="M2 6l3 3 5-6" fill="none" stroke="#f07a1e" stroke-width="2"/></svg>Role-based permissions</li>
      <li><svg viewBox="0 0 12 12"><path d="M2 6l3 3 5-6" fill="none" stroke="#f07a1e" stroke-width="2"/></svg>Centralized billing</li>
      <li><svg viewBox="0 0 12 12"><path d="M2 6l3 3 5-6" fill="none" stroke="#f07a1e" stroke-width="2"/></svg>Multi-usage Mail Merge</li>
    </ul>
    <span class="btn">Buy Now</span>
  </div>
  <div class="abs plan" style="left:780px">
    <div class="plan-head"><h3>Ultra</h3><div class="price"><b>$55</b><span>per user/per month</span></div></div>
    <ul>
      <li><svg viewBox="0 0 12 12"><path d="M2 6l3 3 5-6" fill="none" stroke="#f07a1e" stroke-width="2"/></svg>Includes Pro features and...</li>
      <li><svg viewBox="0 0 12 12"><path d="M2 6l3 3 5-6" fill="none" stroke="#f07a1e" stroke-width="2"/></svg>Presentation tracking &amp; analytics</li>
      <li><svg viewBox="0 0 12 12"><path d="M2 6l3 3 5-6" fill="none" stroke="#f07a1e" stroke-width="2"/></svg>Presentation Analytics reporting</li>
      <li><svg viewBox="0 0 12 12"><path d="M2 6l3 3 5-6" fill="none" stroke="#f07a1e" stroke-width="2"/></svg>Click-to-Call (up to 240 min/user)</li>
      <li><svg viewBox="0 0 12 12"><path d="M2 6l3 3 5-6" fill="none" stroke="#f07a1e" stroke-width="2"/></svg>CRM Sync &amp; Dialer</li>
    </ul>
    <span class="btn">Buy Now</span>
  </div>
</section>

<section class="blogs">
  <div class="abs sec-title" style="top:60px">
    <h2>Our <span class="accent">Blogs</span></h2>
    <div class="underline-mark"><span></span><span></span></div>
    <p>Lorem ipsum dolor sit amet, consectetuer adipiscing elit, sed diam nonummy nibh euismod tincidunt ut laoreet dolore magna aliquam erat volutpat.</p>
  </div>
  <div class="abs blog-grid">
    <div class="blog-img" role="img" aria-label="Hands typing on a laptop with code on screen"><span class="date">08<br>Sep</span></div>
    <div class="blog-txt"><h4>Ipsum Lorem Dolor Sit Amet, Consectetuer...</h4><p>Lorem ipsum dolor sit amet, consectetuer adipiscing elit, sed diam.</p><span class="read">Read More</span></div>
    <div class="blog-img" role="img" aria-label="Hooded figure in a masked disguise in a dark room"><span class="date">08<br>Sep</span></div>
    <div class="blog-txt"><h4>Amet Lorem Dolor Sit, Consectetuer...</h4><p>Lorem ipsum dolor sit amet, consectetuer adipiscing elit, sed diam.</p><span class="read">Read More</span></div>
    <div class="blog-txt"><h4>Lorem Ipsum Dolor Sit Amet, Consectetuer...</h4><p>Lorem ipsum dolor sit amet, consectetuer adipiscing elit, sed diam.</p><span class="read">Read More</span></div>
    <div class="blog-img" role="img" aria-label="Laptop showing security dashboard on a desk"><span class="date">08<br>Sep</span></div>
    <div class="blog-txt"><h4>Lorem Ipsum Dolor Sit Amet, Consectetuer...</h4><p>Lorem ipsum dolor sit amet, consectetuer adipiscing elit, sed diam.</p><span class="read">Read More</span></div>
    <div class="blog-img" role="img" aria-label="Operations room with rows of glowing monitors"><span class="date">08<br>Sep</span></div>
  </div>
  <span class="abs btn">View All</span>
</section>

<section class="news">
  <div class="abs arrow" style="left:140px"><svg width="10" height="10" viewBox="0 0 10 10"><path d="M7 1L3 5l4 4" fill="none" stroke="#f07a1e" stroke-width="1.8"/></svg></div>
  <div class="abs news-card" style="left:160px">
    <div class="img" role="img" aria-label="Team reviewing data on computer screens"></div>
    <div class="meta"><span>08 Sep 2019</span><span>08 Sep 2019</span></div>
    <h4>Lorem ipsum dolor sit amet, consectetuer adipiscing.</h4>
    <span class="read">Read More</span>
  </div>
  <div class="abs news-card" style="left:460px">
    <div class="img" role="img" aria-label="Person working at a laptop in a dim office"></div>
    <div class="meta"><span>08 Sep 2019</span><span>08 Sep 2019</span></div>
    <h4>Lorem ipsum dolor sit amet, consectetuer adipiscing.</h4>
    <span class="read">Read More</span>
  </div>
  <div class="abs arrow" style="left:730px"><svg width="10" height="10" viewBox="0 0 10 10"><path d="M3 1l4 4-4 4" fill="none" stroke="#f07a1e" stroke-width="1.8"/></svg></div>
  <div class="abs news-head">
    <h2>Latest <span class="accent">News</span></h2>
    <div class="underline-mark"><span></span><span></span></div>
    <span class="btn">View All</span>
  </div>
</section>

<section class="contact">
  <div class="abs sec-title" style="top:60px">
    <h2>Contact <span class="accent">Us Now</span></h2>
    <div class="underline-mark"><span></span><span></span></div>
  </div>
  <div class="abs form">
    <div class="field"><svg viewBox="0 0 12 12"><circle cx="6" cy="4" r="2.5" fill="#f07a1e"/><path d="M1 12a5 5 0 0110 0" fill="#f07a1e"/></svg>Your Name*</div>
    <div class="field"><svg viewBox="0 0 12 12"><rect x="1" y="3" width="10" height="8" fill="#f07a1e"/></svg>Company Name*</div>
    <div class="field"><svg viewBox="0 0 12 12"><path d="M2 1h3l1 3-2 1a7 7 0 003 3l1-2 3 1v3a1 1 0 01-1 1A10 10 0 011 2a1 1 0 011-1z" fill="#f07a1e"/></svg>Phone*</div>
    <div class="field tall"><svg viewBox="0 0 12 12"><path d="M1 1h10v7H5l-3 3V8H1z" fill="#f07a1e"/></svg>Message</div>
    <div class="field"><svg viewBox="0 0 12 12"><rect x="1" y="2" width="10" height="8" fill="#f07a1e"/><path d="M1 2l5 4 5-4" fill="none" stroke="#fff"/></svg>Email*</div>
  </div>
  <span class="abs btn">Submit</span>
</section>

<footer class="footer">
  <div class="brand"><i></i>Cindervault</div>
  <p class="abs about-f">Lorem ipsum dolor sit amet, consectetuer adipiscing elit, sed diam nonummy nibh euismod tincidu.</p>
  <div class="abs socials"><i></i><i></i><i></i><i></i></div>
  <div class="abs fcol" style="left:460px">
    <h4>Contact Details</h4>
    <ul class="contact-list">
      <li><svg viewBox="0 0 22 22"><circle cx="11" cy="11" r="11" fill="#f07a1e"/><path d="M11 5a4 4 0 014 4c0 3-4 8-4 8s-4-5-4-8a4 4 0 014-4z" fill="#fff"/></svg><span><b>Address</b>48 Harbour Lane, Sydney<br>NSW 2000</span></li>
      <li><svg viewBox="0 0 22 22"><circle cx="11" cy="11" r="11" fill="#f07a1e"/><path d="M7 6h3l1 3-2 1a6 6 0 003 3l1-2 3 1v3a1 1 0 01-1 1A9 9 0 016 7a1 1 0 011-1z" fill="#fff"/></svg><span><b>Call Us</b>02 5550 1847</span></li>
      <li><svg viewBox="0 0 22 22"><circle cx="11" cy="11" r="11" fill="#f07a1e"/><rect x="6" y="7" width="10" height="8" fill="#fff"/><path d="M6 7l5 4 5-4" fill="none" stroke="#f07a1e"/></svg><span><b>Email Us</b>info@cindervault.com</span></li>
    </ul>
  </div>
  <div class="abs fcol" style="left:720px">
    <h4>Quick Links</h4>
    <ul><li class="on">Home</li><li>About</li><li>Services</li><li>Case Studies</li><li>Blog</li><li>News</li><li>Contact Us</li></ul>
  </div>
  <div class="abs fcol" style="left:880px">
    <h4>Our Services</h4>
    <ul><li>Bug Bounty</li><li>Penetration Testing</li><li>Code Review</li></ul>
  </div>
  <div class="abs copyright">Copyright © 2023 Cindervault. All Rights Reserved.</div>
</footer>

</body>
</html>
```